Lasting Exchange One Pager

We are looking for an introductory one-pager to tell potential customers about our corporate training program. It is called Lasting Exchange. Please see the added files below for detailed specs and requirements. Thank you!
Updates

Project Deadline Extended
Reason: Hi All, We are extending the project by a day, since we had slow submissions over the weekend. We are looking for a design that is pleasing/modern in look and feel - I think that we would prefer it to look artistic rather than corporate or industrial. I"knew to this, so please forgive me if my directions are vague, and please feel free to reach out for feedback.

Industry/Entity Type

Training

```html
<!DOCTYPE html>
<html lang="en">
<head>
<meta charset="utf-8">
<title>Lasting Exchange One Pager</title>
<link rel="stylesheet" href="https://fonts.googleapis.com/css2?family=Questrial&display=swap">
<style>
:root{
  --sky:#33ccff;
  --mist:#dcdce6;
  --ink:#111111;
  --paper:#ffffff;
}
*{margin:0;padding:0;box-sizing:border-box}
html,body{width:1200px;height:849px;overflow:hidden;background:var(--paper)}
.page{position:relative;width:1200px;height:849px;overflow:hidden;background:var(--mist);
  font-family:"Questrial","Century Gothic",sans-serif;color:var(--ink);font-size:16px;line-height:17px}
.backdrop{position:absolute;inset:0}
.intro,.questions-top{position:absolute;text-align:center}
.intro{left:30px;width:550px;top:40px}
.questions-top{left:610px;width:580px;top:45px}
.gap{height:17px}
.badge-text{position:absolute;color:var(--paper);text-align:center;font-size:15.5px;line-height:17px}
.ask{left:55px;width:160px;top:268px}
.value-title{left:655px;width:120px;top:352px}
.quote{position:absolute;left:243px;top:334px;color:var(--paper);font-style:italic;font-size:19.5px;line-height:21px;text-align:center}
.body-left{position:absolute;left:48px;top:417px;width:540px}
.skills{margin-left:104px}
.benefits{position:absolute;left:780px;width:410px;top:335px;text-align:center;list-style:none;line-height:20.35px}
</style>
</head>
<body>
<div class="page">
  <svg class="backdrop" width="1200" height="849" viewBox="0 0 1200 849" aria-hidden="true">
    <path d="M0,243 C120,222 350,225 600,258 C700,236 900,230 1200,268 L1200,849 L0,849 Z" fill="var(--sky)"/>
    <line x1="600" y1="0" x2="600" y2="849" stroke="var(--paper)" stroke-width="1.5" stroke-dasharray="3 4"/>
    <circle cx="135" cy="318" r="80" fill="var(--ink)"/>
    <path d="M190,345 L218,378 L165,390 Z" fill="var(--ink)"/>
    <circle cx="713" cy="362" r="64" fill="var(--ink)"/>
    <circle cx="768" cy="550" r="63" fill="var(--ink)"/>
    <circle cx="700" cy="685" r="50" fill="var(--ink)"/>
  </svg>

  <div class="intro">
    <p>We have 40 years of proven success creating<br>dialogue-based solutions to some of the worlds most entrenched<br>and vexing problems.</p>
    <div class="gap"></div>
    <p>Our program is a 3 week programme held once a week at<br>your place of work.</p>
    <p>Our program is a 3 week programme held once a week at<br>your place of work.</p>
  </div>

  <div class="questions-top">
    <p>What’s the most frustrating thing about your job?</p>
    <p>How can we get traction on our companies most difficult problems?</p>
    <p>How do we ask the right questions to make positive changes?</p>
    <p>I want everyone to bring their authentic self to work</p>
    <p>I want to finally gain traction around that tired problem that has<br>been plaguing my organization</p>
    <p>How can I encourage and enable flow of information so that people<br>can work across differences and do their best?</p>
    <p>What’s the most frustrating thing about your job?</p>
    <p>How can we get traction on our companies most difficult problems?</p>
    <p>How do we ask the right questions to make positive changes?</p>
  </div>

  <p class="badge-text ask">Something<br>needs to change.<br><br>Do you have the<br>tools to get<br>started?</p>
  <p class="quote">In just one hour, we went beyond<br>months of small talk...</p>

  <div class="body-left">
    <p>If you have ever asked yourself any of these questions, we can help<br>you</p>
    <div class="gap"></div>
    <p>What’s the most frustrating thing about your job?</p>
    <p>How can we get traction on our companies most difficult problems?</p>
    <p>How do we ask the right questions to make positive changes?</p>
    <p>I want everyone to bring their authentic self to work</p>
    <p>I want to finally gain traction around that tired problem that has been<br>plaguing my organization</p>
    <p>How can I encourage and enable flow of information so that people<br>can work across differences and do their best?</p>
    <div class="gap"></div>
    <p>The Lasting Exchange Process Is a results-based, step by step<br>process</p>
    <div class="gap"></div>
    <p>You will learn essential life-skills thats</p>
    <div class="skills">
      <p>Inherently Energizing.</p>
      <p>Community Oriented</p>
      <p>Relationship Enhancing</p>
      <p>Culture Building</p>
      <p>Silo-busting</p>
      <p>Simple But Challenging</p>
    </div>
  </div>

  <p class="badge-text value-title">How Lasting<br>Exchange Initiatives<br>Add Value:</p>

  <ul class="benefits">
    <li>Super-charges your conversations</li>
    <li>Creates a shared vision</li>
    <li>Transforms relationships</li>
    <li>Empowers people to design change</li>
    <li>Creates optimal systems</li>
    <li>Delivers unique outcomes</li>
    <li>Supports conflict resolution</li>
    <li>Drives collaboration</li>
    <li>Enhances diversity</li>
    <li>Unites teams</li>
    <li>Uncovers root causes</li>
    <li>Increases innovation</li>
    <li>Ends dysfunctional patterns</li>
    <li>Generates trust</li>
    <li>Cultivates authentic leadership</li>
    <li>Increases engagement</li>
    <li>Promotes peer learning</li>
    <li>Builds resilience</li>
    <li>Activates networks</li>
    <li>Improves the caliber of interactions</li>
    <li>Supports stakeholder and client outcomes</li>
  </ul>
</div>
</body>
</html>
```